medical practice needs a printed banner design

we need a printed banner for a new pain management medical practice in Las Vegas. The name of the practice is "Marlowe Pain Relief Center".
39" x 80" vertical banner
the look should be modern, clean, professional and in line with design of website. Please visit the website for more information regarding the practice.

Target Market(s)

age typically 40+, patients with back pain, joint pain

Industry/Entity Type

Doctor

Requirements
Must have
• our logo (attached file)
• phone number: (702) 555-0187
• website address: marlowepaincareclinic.example
• Hablamos EspaƱol
Nice to have
• slogan: Live Better (banner does not necessarily need to include slogan, but would be preferred)
• maybe a photo of spine, or photo depicting back pain, or active lifestyle
Should not have
• please do not include physical address location as we will be relocating
• * in addition, we hope the banner is not to be misconstrued as a chiropractic
• practice

```html
<!DOCTYPE html>
<html lang="en">
<head>
<meta charset="utf-8">
<title>Marlowe Pain Relief Center – Vertical Banner</title>
<link rel="stylesheet" href="https://fonts.googleapis.com/css2?family=Montserrat:wght@500;600;700;800&family=Open+Sans:wght@400;500&display=swap">
<style>
  :root {
    --navy: #1d2d5a;
    --teal: #2cb5c3;
    --white: #ffffff;
    --photo-light: #f4f1ee;
    --photo-mid: #e6ddd5;
    --photo-warm: #cdb8a6;
  }
  * { margin: 0; padding: 0; box-sizing: border-box; }
  html, body { width: 1200px; height: 2324px; overflow: hidden; background: var(--white); }
  .banner {
    position: relative;
    width: 1200px;
    height: 2324px;
    background: var(--white);
    font-family: "Montserrat", sans-serif;
    color: var(--navy);
    overflow: hidden;
  }
  .top-band {
    position: absolute; left: 0; top: 0; width: 100%; height: 40px;
    background: var(--navy);
  }
  .brand {
    position: absolute; top: 90px; left: 0; width: 100%;
    text-align: center;
  }
  .brand-mark {
    display: block; width: 120px; height: 120px; margin: 0 auto 40px;
    background: var(--teal);
  }
  .brand-name {
    font-weight: 700; font-size: 64px; letter-spacing: 6px; line-height: 1.2;
    color: var(--navy);
  }
  .hero-photo {
    position: absolute; left: 0; top: 540px; width: 100%; height: 700px;
    background:
      radial-gradient(ellipse 320px 460px at 78% 60%, var(--photo-warm) 0%, rgba(205,184,166,0) 70%),
      linear-gradient(180deg, var(--photo-light) 0%, var(--photo-mid) 100%);
  }
  .slogan {
    position: absolute; left: 72px; top: 790px;
    font-weight: 800; font-size: 116px; line-height: 1.05;
    color: var(--navy); text-transform: uppercase;
  }
  .wave {
    position: absolute; left: 0; top: 1100px; width: 1200px; height: 240px;
  }
  .practice-name {
    position: absolute; left: 0; top: 1380px; width: 100%;
    text-align: center; font-weight: 800; font-size: 88px; line-height: 1.25;
    text-transform: uppercase;
  }
  .practice-name .line-navy { display: block; color: var(--navy); }
  .practice-name .line-teal { display: block; color: var(--teal); }
  .language {
    position: absolute; left: 0; top: 1660px; width: 100%;
    text-align: center; font-family: "Open Sans", sans-serif;
    font-weight: 500; font-size: 68px; color: var(--navy);
  }
  .divider {
    position: absolute; left: 300px; top: 1776px; width: 600px; height: 9px;
    background: var(--navy);
  }
  .call-label {
    position: absolute; left: 0; top: 1845px; width: 100%;
    text-align: center; font-weight: 700; font-size: 62px; color: var(--teal);
  }
  .phone {
    position: absolute; left: 0; top: 1935px; width: 100%;
    text-align: center; font-family: "Open Sans", sans-serif;
    font-weight: 500; font-size: 112px; color: var(--navy);
  }
  .bottom-band {
    position: absolute; left: 0; top: 2190px; width: 100%; height: 134px;
    background: var(--navy);
    display: flex; align-items: center; justify-content: center;
  }
  .website {
    font-weight: 600; font-size: 54px; color: var(--white);
  }
</style>
</head>
<body>
  <div class="banner">
    <div class="top-band"></div>

    <header class="brand">
      <span class="brand-mark"></span>
      <div class="brand-name">MARLOWE<br>PAIN RELIEF CENTER</div>
    </header>

    <div class="hero-photo" role="img" aria-label="Photo of a woman seen from behind stretching her arms overhead in a bright room"></div>

    <h1 class="slogan">Live<br>Better</h1>

    <svg class="wave" viewBox="0 0 1200 240" preserveAspectRatio="none" aria-hidden="true">
      <path d="M0 150 C 300 40, 800 40, 1200 110 L1200 240 L0 240 Z" fill="var(--navy)"/>
      <path d="M0 175 C 320 80, 820 75, 1200 135 L1200 240 L0 240 Z" fill="var(--teal)"/>
      <path d="M0 200 C 340 115, 840 110, 1200 160 L1200 240 L0 240 Z" fill="var(--white)"/>
    </svg>

    <h2 class="practice-name">
      <span class="line-navy">Marlowe Pain</span>
      <span class="line-teal">Relief Center</span>
    </h2>

    <p class="language">Hablamos Español</p>
    <div class="divider"></div>

    <p class="call-label">CALL US:</p>
    <p class="phone">(702) 555-0187</p>

    <footer class="bottom-band">
      <span class="website">marlowepaincareclinic.example</span>
    </footer>
  </div>
</body>
</html>
```